The Copper Ladder

we require a classy business card design for a business coaching company that uses our current logo and the wording:

Front of card:

LOGO
Kyle Morrison
CEO
TEL: 1300 4 52918
FAX: 1300 5 52918
Mobile: 0412 638194
PO Box 917, Ferris Hollow, Brisbane, Qld 4127
e: kylem@copperladder.com.au
w: www.copperladder.com.au

Reverse side of the card:

Systematizing Businesses into Turnkey Operations
Strategic Business Plans
Sales & Marketing Programs
Sales Training & Business Coaching
Internet Marketing & Web Design

Here’s what our clients say:

“We grew from $396,000 to over $5million in 4 years and made KTS’s Rising Enterprises Roll 3 years running!” – Martin Greaves, Meridian Works

Target Market(s)

small to medium sized business owners in Australia

Industry/Entity Type

Business

Requirements
Must have
• standard business card size

```html
<!DOCTYPE html>
<html lang="en">
<head>
<meta charset="utf-8">
<title>The Copper Ladder – Business Card</title>
<link rel="stylesheet" href="https://fonts.googleapis.com/css2?family=Arimo:ital,wght@0,400;1,400&family=Tinos:ital,wght@0,400;1,400&display=swap">
<style>
  :root {
    --board-light: #f4f4f4;
    --board-dark: #a9a9a9;
    --card-white: #ffffff;
    --card-fade: #e4e4e4;
    --ink: #1c1c1c;
    --ink-soft: #2e2e2e;
    --accent: #f5b52e;
    --serif: "Tinos", "Times New Roman", serif;
    --sans: "Arimo", Arial, sans-serif;
  }
  * { margin: 0; padding: 0; box-sizing: border-box; }
  html, body { width: 1200px; height: 1200px; overflow: hidden; }
  body {
    position: relative;
    background: radial-gradient(ellipse at 50% 45%, var(--board-light) 0%, #d2d2d2 55%, var(--board-dark) 100%);
    color: var(--ink);
  }
  .side-label {
    position: absolute;
    left: 0; width: 1200px;
    text-align: center;
    font-family: var(--sans);
    font-size: 62px;
    color: #111;
  }
  .side-label--front { top: 28px; }
  .side-label--back { top: 606px; }

  .card {
    position: absolute;
    left: 224px;
    width: 816px;
    height: 460px;
    background: linear-gradient(180deg, var(--card-white) 0%, var(--card-white) 55%, var(--card-fade) 100%);
  }
  .card--front { top: 132px; }
  .card--back { top: 690px; height: 464px; }

  /* Front */
  .brand {
    position: absolute;
    left: 28px; top: 70px;
    width: 300px;
    display: flex; align-items: center; gap: 14px;
  }
  .brand__mark { flex: none; }
  .brand__name {
    font-family: var(--serif);
    font-size: 42px;
    line-height: 1.0;
    color: var(--ink);
  }
  .person {
    position: absolute;
    right: 22px; top: 52px;
    text-align: right;
  }
  .person__name { font-family: var(--serif); font-size: 44px; line-height: 1.1; }
  .person__role { font-family: var(--sans); font-style: italic; font-size: 34px; margin-right: 28px; line-height: 1.2; }

  .contact {
    position: absolute;
    right: 22px; top: 176px;
    text-align: right;
    font-family: var(--sans);
    font-size: 29px;
    line-height: 46px;
  }
  .contact .value { color: var(--accent); }
  .contact__address { font-family: var(--serif); font-size: 30px; }

  .web {
    position: absolute;
    left: 20px; top: 314px;
    font-family: var(--serif);
    font-size: 30px;
    line-height: 46px;
  }
  .web .value { color: var(--accent); }

  /* Back */
  .testimonial {
    position: absolute;
    left: 24px; top: 88px;
    width: 420px;
  }
  .testimonial__intro { font-family: var(--sans); font-style: italic; font-size: 25px; margin-bottom: 28px; }
  .testimonial__quote { font-family: var(--serif); font-size: 26px; line-height: 37px; }
  .testimonial__quote .highlight { color: var(--accent); }

  .services {
    position: absolute;
    right: 16px; top: 88px;
    list-style: none;
    font-family: var(--sans);
    font-size: 25px;
    line-height: 32px;
    text-align: right;
  }
  .services li {
    display: flex; align-items: center; justify-content: flex-end;
    gap: 14px;
    margin-bottom: 14px;
  }
  .services li::after {
    content: "";
    flex: none;
    width: 12px; height: 12px;
    border-radius: 50%;
    background: var(--accent);
  }
</style>
</head>
<body>
  <div class="side-label side-label--front">Front</div>

  <section class="card card--front">
    <div class="brand">
      <svg class="brand__mark" width="26" height="26" viewBox="0 0 26 26" aria-hidden="true">
        <circle cx="13" cy="13" r="12" fill="#1c1c1c"/>
      </svg>
      <div class="brand__name">The Copper Ladder</div>
    </div>

    <div class="person">
      <div class="person__name">Kyle Morrison</div>
      <div class="person__role">CEO</div>
    </div>

    <div class="contact">
      <div>TEL: <span class="value">1300 4 52918</span></div>
      <div>FAX: <span class="value">1300 5 52918</span></div>
      <div>Mobile: <span class="value">0412 638194</span></div>
      <div class="contact__address">PO Box 917, Ferris Hollow,</div>
      <div class="contact__address">Brisbane, Qld 4127</div>
    </div>

    <div class="web">
      <div>e: <span class="value">kylem@copperladder.com.au</span></div>
      <div>w: <span class="value">www.copperladder.com.au</span></div>
    </div>
  </section>

  <div class="side-label side-label--back">Back</div>

  <section class="card card--back">
    <div class="testimonial">
      <p class="testimonial__intro">Here’s what our clients say:</p>
      <p class="testimonial__quote">“We grew <span class="highlight">from $396,000 to over $5million in 4 years</span> and made KTS’s Rising Enterprises Roll 3 years running!” – Martin Greaves, Meridian Works</p>
    </div>

    <ul class="services">
      <li>Systematizing Businesses<br>into Turnkey Operations</li>
      <li>Strategic Business Plans</li>
      <li>Sales &amp; Marketing Programs</li>
      <li>Sales Training &amp;<br>Business Coaching</li>
      <li>Internet Marketing &amp; Web Design</li>
    </ul>
  </section>
</body>
</html>
```